Hydrographic business needs a business card that reaches hunters and off-road enthusiasts

We need a business card for a new hydrographics company catering to customers such as hunters, off-road ATV riders and custom vehicle enthusiasts. A western theme is preferred but professional. Our service should be thought of as upper end graphic design on firearms, off road vehicles, motorcycles, etc... See www.caldorfx.com for ideas on patterns, colors, etc...

Target Market(s)

Hunters, off road enthusiasts, custom car enthusiasts, motorcycle riders...

Industry/Entity Type

Graphic Design

```html
<!DOCTYPE html>
<html lang="en">
<head>
<meta charset="utf-8">
<title>Caldor Hydro Graphics – Business Card Proof</title>
<link rel="stylesheet" href="https://fonts.googleapis.com/css2?family=Smokum&family=Rye&family=Arimo:wght@400;700&display=swap">
<style>
  :root {
    --ink: #1c1712;
    --proof-blue: #2b3dff;
    --rule: #222222;
    --page: #ffffff;
  }
  html, body {
    margin: 0;
    padding: 0;
    width: 1200px;
    height: 1000px;
    overflow: hidden;
    background: var(--page);
  }
  .sheet {
    position: relative;
    width: 1200px;
    height: 1000px;
  }
  .card {
    position: absolute;
    left: 86px;
    top: 105px;
    width: 1050px;
    height: 600px;
  }
  .western { font-family: "Smokum", "Rye", serif; fill: var(--ink); }
  .western-bold { font-family: "Rye", "Smokum", serif; fill: var(--ink); }
  .brand-name { font-family: "Smokum", "Rye", serif; fill: var(--ink); }

  .proof-label {
    position: absolute;
    left: 28px;
    top: 784px;
    font-family: "Arimo", Arial, sans-serif;
    font-weight: 700;
    font-size: 29px;
    color: #000;
    letter-spacing: 0.5px;
  }
  .proof-band {
    position: absolute;
    left: 155px;
    top: 787px;
    width: 1023px;
    height: 26px;
    background: var(--proof-blue);
  }
  .proof-box {
    position: absolute;
    top: 832px;
    width: 282px;
    height: 138px;
    border: 1px solid var(--rule);
    box-sizing: border-box;
    font-family: "Arimo", Arial, sans-serif;
    font-size: 16px;
    color: #111;
  }
  .proof-box .box-title {
    position: absolute;
    left: 4px;
    top: 1px;
  }
  .proof-box .box-value {
    position: absolute;
    left: 16px;
    top: 39px;
  }
  .box-prepared { left: 248px; }
  .box-colors { left: 572px; }
  .box-notes { left: 894px; }
  .swatch {
    position: absolute;
    left: 102px;
    top: 33px;
    width: 55px;
    height: 55px;
    border-radius: 9px;
    background: #0a0a0a;
  }
  .swatch-code {
    position: absolute;
    left: 0;
    width: 100%;
    top: 103px;
    text-align: center;
  }
</style>
</head>
<body>
<main class="sheet">
  <svg class="card" viewBox="0 0 1050 600" xmlns="http://www.w3.org/2000/svg" aria-label="Caldor Hydro Graphics business card">
    <defs>
      <radialGradient id="parchment" cx="50%" cy="45%" r="75%">
        <stop offset="0%" stop-color="#f3e6c2"/>
        <stop offset="55%" stop-color="#e6cf98"/>
        <stop offset="100%" stop-color="#b98c4e"/>
      </radialGradient>
      <radialGradient id="badgeFill" cx="40%" cy="35%" r="70%">
        <stop offset="0%" stop-color="#d4a752"/>
        <stop offset="100%" stop-color="#8a6020"/>
      </radialGradient>
    </defs>

    <rect class="card-background" x="0" y="0" width="1050" height="600" fill="url(#parchment)" role="img" aria-label="Aged parchment paper texture"/>

    <text class="western card-title" x="525" y="86" text-anchor="middle" font-size="76" textLength="940" lengthAdjust="spacingAndGlyphs">CALDOR HYDRO GRAPHICS</text>
    <text class="western-bold card-tagline" x="519" y="124" text-anchor="middle" font-size="21" textLength="810" lengthAdjust="spacingAndGlyphs">THE BEST AND MOST RELIABLE HYDROGRAPHICS SERVICE IN TEXAS</text>

    <text class="western contact-name" x="278" y="232" text-anchor="middle" font-size="44" textLength="244" lengthAdjust="spacingAndGlyphs">WADE CALDOR</text>
    <text class="western-bold contact-phone" x="278" y="327" text-anchor="middle" font-size="50" textLength="282" lengthAdjust="spacingAndGlyphs">555.014.2287</text>
    <text class="western contact-street" x="278" y="398" text-anchor="middle" font-size="42" textLength="494" lengthAdjust="spacingAndGlyphs">212 MESQUITE COUNTY ROAD 4120</text>
    <text class="western contact-city" x="278" y="467" text-anchor="middle" font-size="46" textLength="440" lengthAdjust="spacingAndGlyphs">CEDAR BLUFF, TX 75010</text>

    <text class="western contact-email" x="92" y="577" font-size="44" textLength="408" lengthAdjust="spacingAndGlyphs">WADE@CALDORFX.COM</text>
    <text class="western contact-web" x="567" y="577" font-size="44" textLength="390" lengthAdjust="spacingAndGlyphs">WWW.CALDORFX.COM</text>

    <g class="brand-mark">
      <circle cx="792" cy="335" r="196" fill="url(#badgeFill)"/>
      <text class="brand-name" x="792" y="348" text-anchor="middle" font-size="34" textLength="320" lengthAdjust="spacingAndGlyphs">CALDOR HYDRO GRAPHICS</text>
    </g>
  </svg>

  <div class="proof-label">PROOF</div>
  <div class="proof-band"></div>

  <section class="proof-box box-prepared">
    <span class="box-title">Prepared For:</span>
    <span class="box-value">Caldor Hydro Graphics</span>
  </section>
  <section class="proof-box box-colors">
    <span class="box-title">Colors Used:</span>
    <div class="swatch"></div>
    <span class="swatch-code">000000</span>
  </section>
  <section class="proof-box box-notes">
    <span class="box-title">Notes:</span>
  </section>
</main>
</body>
</html>
```